Hello Creative Minds!
Our business is after a elegant and classy flyer that draws attention!
The business is Velmora Turf - Lawn Rejuvenation Services. We provide services that maintain a healthy and vibrant green lawn through the tough Australian seasons. The products we use limits the water needed to keep grass green to a minimum - practically none at all! This not only helps the home owner or home seller but the environment by limiting the use of water that is needed to create a green lawn. The products we use are made from natural ingredients that are and pet friendly.
This fly will be our introductory offer to the market. Below are the required points that need to be on the flyer. Attached is the business logo, before & after pictures and 1 example of the LAYOUT not DESIGN of what the flyer should be laid out like or similar to. Feel free to use different 'Lawn Mower' pictures.
All the best; if you need any questions answered please feel free to message.
REQUIRED POINTS (Please re-phrase were possible);
*Instantly restores the natural green colour of grass – year round
*Lasts for up to 3 months
*Substantially reduces watering needs
*Pet friendly
*Stays green during droughts and water restrictions
*UV fade resistant
*Won’t bleed, run, or stain once absorbed into the grass
*Safe for the environment, pets and people
*Works in extreme heat, cold and frost
*Organic and natural – no harmful chemicals
*Reduces the amount of fertilizer
and water used on lawns
*Kerb appeal is essential for getting your property sold for the highest price possible
SERVICES & PRICING
Lawn maintenance (cut & trim) starting from $60
Lawn rejuvenation starting from $80 (Only $27 a month for 3 months)*
Package deal starting from $120
Introductory offer: 25% off all services. Refer a friend, when they book you receive another 25% off your next service.
LOCATIONS
Nowra to Sydney
CONTACT NUMBER
Will be posted with the winner - please leave an area for this.
SOCIAL MEDIA
Please add Chatterloop and Snapvista logo's
Updates
Competition has finished, thank you to all that have participated! I will review and comment on the flyers that need assistance. All the best with future designs!
Target Market(s)
home owners, home sellers, property developers, real estates and nursing homes and government housing.
Industry/Entity Type
Lawn Care
Look and feel
Each slider illustrates characteristics of the customer's brand and the style your logo design should communicate.

```html
<!DOCTYPE html>
<html lang="en">
<head>
<meta charset="utf-8">
<title>Velmora Turf - Lawn Rejuvenation Services</title>
<link href="https://fonts.googleapis.com/css2?family=Montserrat:wght@400;500;600;700&family=Oswald:wght@300;400;500;600;700&family=Roboto+Condensed:wght@400;700&display=swap" rel="stylesheet">
<style>
:root{
  --charcoal:#2b2f38;
  --charcoal-dark:#23262e;
  --offer-red:#d7141a;
  --deep-green:#0f6b14;
  --band-green:#1f9a22;
  --lime:#9fd84a;
  --meadow:#8cc63f;
  --price-green:#2f8f1a;
  --ink:#111;
  --white:#fff;
  --backdrop:#e6e7e9;
}
*{box-sizing:border-box;margin:0;padding:0}
html,body{width:1200px;height:856px;overflow:hidden;background:var(--backdrop)}
body{position:relative;font-family:'Montserrat',sans-serif}
.page{position:absolute;top:21px;width:576px;height:814px;overflow:hidden;background:var(--meadow)}
.page--front{left:17px}
.page--back{left:607px}
.masthead{position:absolute;left:0;top:0;width:100%;height:152px;background:linear-gradient(180deg,#343944,var(--charcoal-dark));text-align:center;color:var(--white)}
.brand-name{position:absolute;left:0;right:0;top:52px;font-family:'Montserrat',sans-serif;font-weight:600;font-size:50px;letter-spacing:1px;line-height:1}
.brand-tagline{position:absolute;left:0;right:0;top:117px;font-size:10.5px;font-weight:500;letter-spacing:4.2px}
.photo{position:absolute;left:0;width:100%}
.photo--home{top:152px;height:397px;background:linear-gradient(180deg,#cfe3b8 0%,#c9b89a 30%,#a3b57a 52%,#4fae2c 70%,#3a9a22 100%)}
.photo--mowing{top:152px;height:364px;background:radial-gradient(ellipse at 75% 40%,#5a9a3a 0%,#2f7a22 45%,#1d5f18 100%)}
.offer{position:absolute;left:0;top:152px;height:66px;width:300px;display:flex;color:var(--white)}
.offer svg{position:absolute;left:0;top:0}
.offer-main{position:relative;width:148px;text-align:center;font-family:'Oswald',sans-serif;padding-top:4px;border-right:2px dotted rgba(255,255,255,.8);line-height:1.12}
.offer-main .title{font-size:16px;font-weight:500}
.offer-main .deal{font-family:'Montserrat',sans-serif;font-size:17px;font-weight:700}
.offer-main .scope{font-size:16px}
.offer-refer{position:relative;width:140px;text-align:center;font-family:'Roboto Condensed',sans-serif;font-size:10.5px;line-height:1.35;padding-top:10px}
.offer-refer b{font-weight:700}
.hero-copy{position:absolute;right:14px;text-align:right;font-family:'Oswald',sans-serif;line-height:1}
.hero-copy--service{top:368px;font-weight:300;font-size:29px;color:var(--white)}
.hero-copy--maintain{top:410px;font-weight:700;font-size:29px;color:var(--deep-green)}
.hero-copy--vibrant{top:442px;font-weight:700;font-size:22.5px;color:var(--deep-green)}
.season-band{position:absolute;left:0;top:471px;width:100%;height:78px;background:var(--band-green)}
.hero-copy--tough{top:478px;font-weight:700;font-size:31px;color:var(--white)}
.hero-copy--aus{top:512px;font-weight:700;font-size:27px;color:var(--white)}
.lower{position:absolute;left:0;width:100%;bottom:0;background:linear-gradient(180deg,var(--meadow) 0%,#86c43a 60%,#3e9d23 100%)}
.page--front .lower{top:549px}
.page--back .lower{top:516px}
.pill{position:absolute;height:31px;border-radius:16px;font-family:'Montserrat',sans-serif;font-weight:700;font-size:17px;display:flex;align-items:center;justify-content:center;letter-spacing:.3px}
.pill--about{left:12px;top:596px;width:143px;background:var(--deep-green);color:var(--lime)}
.pill--benefits{left:12px;top:274px;width:143px;background:var(--lime);color:var(--deep-green)}
.pill--pricing{left:169px;top:517px;width:235px;height:30px;background:var(--deep-green);color:var(--lime);font-size:16.5px}
.about-text{position:absolute;left:176px;top:562px;width:386px;font-size:10.4px;line-height:1.24;text-align:justify;color:var(--ink);padding-left:8px;border-left:2px dotted #3a6a1f}
.call{position:absolute;font-family:'Oswald',sans-serif;line-height:1}
.call--front{left:14px;top:643px}
.call--front .label{font-size:34px;color:var(--white);font-weight:500}
.call--front .number{font-size:25px;color:var(--ink);margin-top:4px;letter-spacing:.5px}
.call--back{left:243px;top:752px;white-space:nowrap}
.call--back .label{font-size:38px;color:var(--white);font-weight:500}
.call--back .number{font-size:29px;color:var(--ink);margin-left:6px;letter-spacing:.5px}
.shot{position:absolute;border:3px solid var(--white)}
.shot--yard-before{left:272px;top:659px;width:102px;height:52px;background:linear-gradient(180deg,#555 0%,#9aa07a 55%,#7a7a70 100%)}
.shot--yard-after{left:272px;top:711px;width:102px;height:52px;background:linear-gradient(180deg,#666 0%,#5aa036 55%,#6e6e68 100%)}
.shot--lawn{left:401px;top:656px;width:158px;height:106px;display:flex;padding:0}
.shot--lawn span{flex:1}
.shot--lawn .dry{background:linear-gradient(135deg,#d8c48a,#b59a5c)}
.shot--lawn .lush{background:linear-gradient(135deg,#5aa83a,#2f7a22);border-left:3px solid var(--white)}
.side-label{position:absolute;left:254px;font-family:'Montserrat',sans-serif;font-weight:700;font-size:10px;color:var(--ink);writing-mode:vertical-rl;transform:rotate(180deg);letter-spacing:.5px}
.side-label--before{top:662px}
.side-label--after{top:722px}
.under-label{position:absolute;top:771px;font-weight:700;font-size:11px;color:var(--ink)}
.under-label--before{left:417px}
.under-label--after{left:499px}
.shot--mower{left:238px;top:640px;width:92px;height:92px;background:linear-gradient(180deg,#3f8a2c,#6ec03d)}
.shot--trimming{left:351px;top:640px;width:92px;height:92px;background:linear-gradient(180deg,#3a6e2a,#7a8a3a)}
.shot--hedge{left:463px;top:640px;width:92px;height:92px;background:linear-gradient(180deg,#2f6a24,#5aa83a)}
.contact{position:absolute;left:0;top:720px;width:240px;height:94px;background:var(--charcoal);border-top-right-radius:22px;color:var(--white);padding:10px 0 0 12px;font-size:11px}
.contact-row{display:flex;align-items:center;gap:6px;height:25px;white-space:nowrap}
.contact-row .key{color:var(--lime);font-weight:500}
.contact-row b{font-weight:600}
.follow{font-size:11.5px;gap:4px}
.follow .lead{margin-right:3px}
.social-dot{width:10px;height:10px;border-radius:50%;background:var(--lime);display:inline-block;flex:none}
.social-name{font-size:9px;font-weight:600;margin-right:3px}
.benefits{position:absolute;left:14px;top:318px;list-style:none}
.benefits li{display:flex;align-items:center;gap:8px;height:15.5px;font-size:10.4px;font-weight:700;color:var(--white)}
.pricing{position:absolute;left:0;right:0;top:549px;text-align:center;font-family:'Roboto Condensed',sans-serif;font-size:15.5px;line-height:23.5px;color:var(--ink)}
.pricing strong{color:var(--price-green);font-weight:700;letter-spacing:.3px}
</style>
</head>
<body>

<section class="page page--front">
  <header class="masthead">
    <div class="brand-name">Velmora Turf</div>
    <div class="brand-tagline">LAWN REJUVENATION SERVICES</div>
  </header>
  <div class="photo photo--home" role="img" aria-label="Photo of a two-storey home with a lush green front lawn and a red lawn mower in the foreground"></div>
  <div class="offer">
    <svg width="300" height="66" aria-hidden="true"><polygon points="0,0 300,0 266,66 0,66" fill="var(--offer-red)"/></svg>
    <div class="offer-main"><div class="title">Introductory Offer</div><div class="deal">25% OFF</div><div class="scope">all services</div></div>
    <div class="offer-refer">Refer a friend, when they<br>book you receive another<br><b>25% OFF</b> your next service.</div>
  </div>
  <div class="hero-copy hero-copy--service">LAWN REJUVENATION SERVICES</div>
  <div class="hero-copy hero-copy--maintain">MAINTAIN A HEALTHY</div>
  <div class="hero-copy hero-copy--vibrant">AND VIBRANT GREEN LAWN</div>
  <div class="season-band"></div>
  <div class="hero-copy hero-copy--tough">THROUGH THE TOUGH</div>
  <div class="hero-copy hero-copy--aus">AUSTRALIAN SEASONS</div>
  <div class="lower"></div>
  <div class="pill pill--about">ABOUT US</div>
  <p class="about-text">We provide services that maintain a healthy and vibrant green lawn through the tough Australian seasons. The products we use limits the water needed to keep grass green to a minimum - practically none at all! This not only helps the home owner or home seller but the environment by limiting the use of water that is needed to create a green lawn. The products we use are made from natural ingredients that are and pet friendly.</p>
  <div class="call call--front"><div class="label">Call us on</div><div class="number">122-000-122</div></div>
  <div class="side-label side-label--before">BEFORE</div>
  <div class="side-label side-label--after">AFTER</div>
  <div class="shot shot--yard-before" role="img" aria-label="Before photo of a patchy backyard lawn"></div>
  <div class="shot shot--yard-after" role="img" aria-label="After photo of the same backyard lawn restored to green"></div>
  <div class="shot shot--lawn" role="img" aria-label="Close-up of dry straw-coloured grass beside rejuvenated green grass"><span class="dry"></span><span class="lush"></span></div>
  <div class="under-label under-label--before">BEFORE</div>
  <div class="under-label under-label--after">AFTER</div>
  <div class="contact">
    <div class="contact-row"><svg width="14" height="17" viewBox="0 0 14 17" aria-hidden="true"><path d="M7 0C3.1 0 0 3 0 6.8 0 11.5 7 17 7 17s7-5.5 7-10.2C14 3 10.9 0 7 0z" fill="var(--lime)"/><circle cx="7" cy="6.6" r="2.6" fill="var(--charcoal)"/></svg><span class="key">LOCATIONS</span><b>Nowra to Sydney</b></div>
    <div class="contact-row"><svg width="15" height="11" viewBox="0 0 15 11" aria-hidden="true"><rect width="15" height="11" rx="1" fill="var(--lime)"/><path d="M0.5 1l7 5 7-5" stroke="var(--charcoal)" stroke-width="1.4" fill="none"/></svg><b>hello@velmoraturf.example</b></div>
    <div class="contact-row follow"><span class="lead">follow us on</span><span class="social-dot"></span><span class="social-name">Chatterloop</span><span class="social-dot"></span><span class="social-name">Snapvista</span></div>
  </div>
</section>

<section class="page page--back">
  <header class="masthead">
    <div class="brand-name">Velmora Turf</div>
    <div class="brand-tagline">LAWN REJUVENATION SERVICES</div>
  </header>
  <div class="photo photo--mowing" role="img" aria-label="Photo of a gardener pushing a green lawn mower across a garden lawn"></div>
  <div class="offer">
    <svg width="300" height="66" aria-hidden="true"><polygon points="0,0 300,0 266,66 0,66" fill="var(--offer-red)"/></svg>
    <div class="offer-main"><div class="title">Introductory Offer</div><div class="deal">25% OFF</div><div class="scope">all services</div></div>
    <div class="offer-refer">Refer a friend, when they<br>book you receive another<br><b>25% OFF</b> your next service.</div>
  </div>
  <div class="pill pill--benefits">BENEFITS</div>
  <ul class="benefits">
    <li><svg width="11" height="11" viewBox="0 0 11 11" aria-hidden="true"><rect x=".6" y=".6" width="9.8" height="9.8" fill="none" stroke="#fff" stroke-width="1.2"/><path d="M2.5 5.5l2.2 2.2 5.5-6" stroke="#fff" stroke-width="1.6" fill="none"/></svg>Instantly restores the natural green colour of grass - year round</li>
    <li><svg width="11" height="11" viewBox="0 0 11 11" aria-hidden="true"><rect x=".6" y=".6" width="9.8" height="9.8" fill="none" stroke="#fff" stroke-width="1.2"/><path d="M2.5 5.5l2.2 2.2 5.5-6" stroke="#fff" stroke-width="1.6" fill="none"/></svg>Lasts for up to 3 months</li>
    <li><svg width="11" height="11" viewBox="0 0 11 11" aria-hidden="true"><rect x=".6" y=".6" width="9.8" height="9.8" fill="none" stroke="#fff" stroke-width="1.2"/><path d="M2.5 5.5l2.2 2.2 5.5-6" stroke="#fff" stroke-width="1.6" fill="none"/></svg>Substantially reduces watering needs</li>
    <li><svg width="11" height="11" viewBox="0 0 11 11" aria-hidden="true"><rect x=".6" y=".6" width="9.8" height="9.8" fill="none" stroke="#fff" stroke-width="1.2"/><path d="M2.5 5.5l2.2 2.2 5.5-6" stroke="#fff" stroke-width="1.6" fill="none"/></svg>Pet friendly</li>
    <li><svg width="11" height="11" viewBox="0 0 11 11" aria-hidden="true"><rect x=".6" y=".6" width="9.8" height="9.8" fill="none" stroke="#fff" stroke-width="1.2"/><path d="M2.5 5.5l2.2 2.2 5.5-6" stroke="#fff" stroke-width="1.6" fill="none"/></svg>Stays green during droughts and water restrictions</li>
    <li><svg width="11" height="11" viewBox="0 0 11 11" aria-hidden="true"><rect x=".6" y=".6" width="9.8" height="9.8" fill="none" stroke="#fff" stroke-width="1.2"/><path d="M2.5 5.5l2.2 2.2 5.5-6" stroke="#fff" stroke-width="1.6" fill="none"/></svg>UV fade resistant</li>
    <li><svg width="11" height="11" viewBox="0 0 11 11" aria-hidden="true"><rect x=".6" y=".6" width="9.8" height="9.8" fill="none" stroke="#fff" stroke-width="1.2"/><path d="M2.5 5.5l2.2 2.2 5.5-6" stroke="#fff" stroke-width="1.6" fill="none"/></svg>Won't bleed, run, or stain once absorbed into the grass</li>
    <li><svg width="11" height="11" viewBox="0 0 11 11" aria-hidden="true"><rect x=".6" y=".6" width="9.8" height="9.8" fill="none" stroke="#fff" stroke-width="1.2"/><path d="M2.5 5.5l2.2 2.2 5.5-6" stroke="#fff" stroke-width="1.6" fill="none"/></svg>Safe for the environment, pets and people</li>
    <li><svg width="11" height="11" viewBox="0 0 11 11" aria-hidden="true"><rect x=".6" y=".6" width="9.8" height="9.8" fill="none" stroke="#fff" stroke-width="1.2"/><path d="M2.5 5.5l2.2 2.2 5.5-6" stroke="#fff" stroke-width="1.6" fill="none"/></svg>Works in extreme heat, cold and frost</li>
    <li><svg width="11" height="11" viewBox="0 0 11 11" aria-hidden="true"><rect x=".6" y=".6" width="9.8" height="9.8" fill="none" stroke="#fff" stroke-width="1.2"/><path d="M2.5 5.5l2.2 2.2 5.5-6" stroke="#fff" stroke-width="1.6" fill="none"/></svg>Organic and natural - no harmful chemicals</li>
    <li><svg width="11" height="11" viewBox="0 0 11 11" aria-hidden="true"><rect x=".6" y=".6" width="9.8" height="9.8" fill="none" stroke="#fff" stroke-width="1.2"/><path d="M2.5 5.5l2.2 2.2 5.5-6" stroke="#fff" stroke-width="1.6" fill="none"/></svg>Reduces the amount of fertilizer and water used on lawns</li>
    <li><svg width="11" height="11" viewBox="0 0 11 11" aria-hidden="true"><rect x=".6" y=".6" width="9.8" height="9.8" fill="none" stroke="#fff" stroke-width="1.2"/><path d="M2.5 5.5l2.2 2.2 5.5-6" stroke="#fff" stroke-width="1.6" fill="none"/></svg>Kerb appeal is essential for getting your property sold for the highest price possible</li>
  </ul>
  <div class="lower"></div>
  <div class="pill pill--pricing">SERVICES &amp; PRICING</div>
  <div class="pricing">
    <div>Lawn maintenance (cut &amp; trim) <strong>starting from $60</strong></div>
    <div>Lawn rejuvenation <strong>starting from $80 (Only $27 a month for 3 months)*</strong></div>
    <div>Package deal <strong>starting from $120</strong></div>
  </div>
  <div class="shot shot--mower" role="img" aria-label="Photo of a lawn mower on green grass"></div>
  <div class="shot shot--trimming" role="img" aria-label="Photo of a gardener trimming plants"></div>
  <div class="shot shot--hedge" role="img" aria-label="Photo of a gardener clipping a hedge"></div>
  <div class="contact">
    <div class="contact-row"><svg width="14" height="17" viewBox="0 0 14 17" aria-hidden="true"><path d="M7 0C3.1 0 0 3 0 6.8 0 11.5 7 17 7 17s7-5.5 7-10.2C14 3 10.9 0 7 0z" fill="var(--lime)"/><circle cx="7" cy="6.6" r="2.6" fill="var(--charcoal)"/></svg><span class="key">LOCATIONS</span><b>Nowra to Sydney</b></div>
    <div class="contact-row"><svg width="15" height="11" viewBox="0 0 15 11" aria-hidden="true"><rect width="15" height="11" rx="1" fill="var(--lime)"/><path d="M0.5 1l7 5 7-5" stroke="var(--charcoal)" stroke-width="1.4" fill="none"/></svg><b>hello@velmoraturf.example</b></div>
    <div class="contact-row follow"><span class="lead">follow us on</span><span class="social-dot"></span><span class="social-name">Chatterloop</span><span class="social-dot"></span><span class="social-name">Snapvista</span></div>
  </div>
  <div class="call call--back"><span class="label">Call us on</span><span class="number">122-000-122</span></div>
</section>

</body>
</html>
```